BLMRC redesign and update stationary bc envelopes.

Stationary, Envelopes, Brochures, Business Card. Need to add second surgeon and two other offices. I need everything to match. I am a oral & maxillofacial surgeon.
Additional surgeon and three office addresses.
Yu Jin Park, DMD, MD, INC

3187 Silver Meadow Parkway
Cedar Ridge, CA 95118

612 Lorin Way, Suite 101
Marlow, CA. 95241

2375 Birch Avenue, Suite 105
Linden Falls, CA. 95377
Updates

Logo design uploaded. Zapfino Extra/Adobe Garamond/Palatino are fonts used before. Not sure what is on exisiting stationary.

Target Market(s)

Referral dentist and sometimes patients. I am a oral & Maxillofacial surgeon.

Industry/Entity Type

Dental Clinic

Font styles to use
Serif
Script

Requirements
Must have
• Color of existing stationary. Update is possible.
Nice to have
• Conservative/modern
Should not have
• Playful

```html
<!DOCTYPE html>
<html lang="en">
<head>
<meta charset="utf-8">
<title>BLMRC Stationery</title>
<link rel="stylesheet" href="https://fonts.googleapis.com/css2?family=Crimson+Text:ital,wght@0,400;0,600;0,700;1,400;1,600&display=swap">
<style>
  :root {
    --brown: #674e3f;
    --ink: #4b3325;
    --green: #6b9a2c;
    --paper: #ffffff;
    --bg: #ffffff;
    --mark: #cfe0b4;
  }
  * { margin: 0; padding: 0; box-sizing: border-box; }
  html, body { width: 1200px; height: 1000px; overflow: hidden; background: var(--bg); }
  body { position: relative; font-family: "Crimson Text", serif; color: var(--ink); }
  .sheet { position: absolute; background: var(--paper); box-shadow: 2px 3px 8px rgba(0,0,0,.22); overflow: hidden; }
  .abs { position: absolute; white-space: nowrap; }
  .center { text-align: center; }
  .band { position: absolute; background: var(--brown); }
  .rule { position: absolute; }
  .name { color: var(--green); font-style: italic; font-weight: 600; }
  .white { color: #fff; }
  .brand { display: flex; align-items: center; gap: 8px; justify-content: center; color: var(--ink); font-weight: 600; letter-spacing: .06em; }
  .brand-dot { border-radius: 50%; background: var(--mark); flex: none; }
  .sep { padding: 0 3px; }

  /* Letterhead */
  .letterhead { left: 77px; top: 62px; width: 620px; height: 876px; }
  .letterhead .brand { position: absolute; left: 0; width: 620px; top: 95px; font-size: 40px; }
  .letterhead .brand-dot { width: 30px; height: 30px; }
  .letterhead .tagline { left: 0; width: 620px; top: 139px; font-size: 15px; font-weight: 700; }
  .letterhead .head-rule { left: 36px; top: 168px; width: 549px; border-top: 1.5px solid var(--ink); }
  .letterhead .doc-left { left: 36px; top: 176px; font-size: 15px; }
  .letterhead .doc-right { right: 35px; top: 176px; font-size: 15px; }
  .letterhead .email { left: 36px; top: 195px; font-size: 8px; font-weight: 600; }
  .letterhead .offices { left: 20px; width: 580px; top: 758px; display: flex; justify-content: center; font-size: 8.5px; line-height: 11px; font-weight: 600; }
  .letterhead .office { padding: 0 6px; text-align: center; }
  .letterhead .office + .office { border-left: 1px solid var(--green); }
  .letterhead .band { left: 0; top: 788px; width: 620px; height: 88px; }
  .letterhead .services { left: 0; width: 620px; top: 795px; font-size: 9px; line-height: 11px; font-weight: 600; }
  .letterhead .band-rule { left: 36px; top: 827px; width: 549px; border-top: 1px solid #fff; }
  .letterhead .site { left: 0; width: 620px; top: 835px; font-size: 14.5px; font-weight: 700; letter-spacing: .02em; }

  /* Business card front */
  .card-front { left: 783px; top: 112px; width: 262px; height: 150px; }
  .card-front .brand { position: absolute; left: 14px; width: 108px; top: 62px; font-size: 17px; gap: 5px; }
  .card-front .brand-dot { width: 13px; height: 13px; }
  .card-front .divider { left: 124px; top: 25px; height: 76px; border-left: 1.5px solid var(--ink); }
  .card-front .doc-a { left: 131px; top: 26px; font-size: 9.5px; }
  .card-front .email { left: 131px; top: 40px; font-size: 5.5px; font-weight: 600; }
  .card-front .doc-b { left: 131px; top: 64px; font-size: 9.5px; }
  .card-front .badge { left: 131px; top: 93px; width: 12px; height: 12px; border-radius: 50%; border: 1.5px solid #555; }
  .card-front .badge-text { left: 147px; top: 92px; font-size: 5px; line-height: 6px; color: #333; }
  .card-front .band { left: 0; top: 124px; width: 262px; height: 26px; }
  .card-front .tagline { left: 0; width: 262px; top: 129px; font-size: 9px; font-weight: 700; }

  /* Business card back */
  .card-back { left: 783px; top: 284px; width: 262px; height: 149px; }
  .card-back .addr { left: 0; width: 262px; font-size: 6.5px; line-height: 8px; font-weight: 600; }
  .card-back .green-rule { left: 37px; width: 188px; border-top: 1px solid var(--green); }
  .card-back .services { left: 0; width: 262px; top: 96px; font-size: 5.3px; line-height: 8px; font-weight: 600; }
  .card-back .band { left: 0; top: 124px; width: 262px; height: 25px; }
  .card-back .site { left: 0; width: 262px; top: 128px; font-size: 9px; font-weight: 700; letter-spacing: .02em; }

  /* Envelope */
  .envelope { left: 444px; top: 466px; width: 678px; height: 324px; }
  .envelope .brand { position: absolute; left: 36px; width: 120px; top: 48px; font-size: 20px; gap: 6px; }
  .envelope .brand-dot { width: 15px; height: 15px; }
  .envelope .tagline { left: 36px; width: 120px; top: 101px; font-size: 7.5px; font-weight: 700; }
  .envelope .divider { left: 158px; top: 29px; height: 88px; border-left: 1.5px solid var(--ink); }
  .envelope .doc-a { left: 168px; top: 28px; font-size: 11.5px; }
  .envelope .doc-b { left: 168px; top: 49px; font-size: 11.5px; }
  .envelope .addr { left: 168px; font-size: 6.5px; font-weight: 600; }
  .envelope .green-rule { left: 168px; width: 171px; border-top: 1px solid var(--green); }
  .envelope .services { left: 0; width: 678px; top: 246px; font-size: 9px; line-height: 11px; font-weight: 600; }
  .envelope .band { left: 14px; top: 275px; width: 650px; height: 29px; }
  .envelope .site { left: 14px; width: 650px; top: 281px; font-size: 12px; font-weight: 700; letter-spacing: .02em; }
</style>
</head>
<body>

<section class="sheet letterhead" aria-label="Letterhead">
  <div class="brand"><span class="brand-dot"></span>BLMRC</div>
  <p class="abs center tagline">Dental Implants and Oral Surgery</p>
  <div class="rule head-rule"></div>
  <p class="abs name doc-left">Martin K. Hale, DDS, Inc.</p>
  <p class="abs name doc-right">Yu Jin Park, DMD, MD, Inc.</p>
  <p class="abs email">mhale@silvermeadowsurgery.com</p>

  <div class="abs offices">
    <div class="office">3187 Silver Meadow Parkway, Cedar Ridge, CA 95118<br>Tel 916.555.0142 / Fax 916.555.0187</div>
    <div class="office">612 Lorin Way, Suite 101, Marlow, CA. 95241<br>Tel 916.555.0163 / Fax 916.555.0164</div>
    <div class="office">2375 Birch Avenue, Suite 105, Linden Falls, CA. 95377<br>Tel 530.555.0119 / Fax 530.555.0126</div>
  </div>
  <div class="band"></div>
  <p class="abs center white services">Dentoalveolar Surgery<span class="sep">•</span>Dental Implant Surgery<span class="sep">•</span>Orthognathic Surgery<span class="sep">•</span>Facial Trauma Surgery<br>Preprosthetic and Reconstructive Surgery<span class="sep">•</span>Temporomandibular Joint Disorders and Surgery<span class="sep">•</span>Obstructive Sleep Apnea Surgery</p>
  <div class="rule band-rule"></div>
  <p class="abs center white site">www.silvermeadowsurgery.com</p>
</section>

<section class="sheet card-front" aria-label="Business card front">
  <div class="brand"><span class="brand-dot"></span>BLMRC</div>
  <div class="rule divider"></div>
  <p class="abs name doc-a">Martin K. Hale, DDS, Inc.</p>
  <p class="abs email">mhale@silvermeadowsurgery.com</p>
  <p class="abs name doc-b">Yu Jin Park, DMD, MD, Inc.</p>
  <div class="abs badge"></div>
  <p class="abs badge-text">Fellows of the National Board of<br>Oral Surgery</p>
  <div class="band"></div>
  <p class="abs center white tagline">Dental Implants and Oral Surgery</p>
</section>

<section class="sheet card-back" aria-label="Business card back">
  <p class="abs center addr" style="top:24px">3187 Silver Meadow Parkway, Cedar Ridge, CA 95118<br>Tel 916.555.0142 • Fax 916.555.0187</p>
  <div class="rule green-rule" style="top:44px"></div>
  <p class="abs center addr" style="top:48px">612 Lorin Way, Suite 101, Marlow, CA. 95241<br>Tel 916.555.0163 • Fax 916.555.0164</p>
  <div class="rule green-rule" style="top:68px"></div>
  <p class="abs center addr" style="top:72px">2375 Birch Avenue, Suite 105, Linden Falls, CA. 95377<br>Tel 530.555.0119 • Fax 530.555.0126</p>
  <p class="abs center services">Dentoalveolar Surgery • Dental Implant Surgery • Orthognathic Surgery<br>Facial Trauma Surgery • Preprosthetic and Reconstructive Surgery<br>Temporomandibular Joint Disorders and Surgery • Obstructive Sleep Apnea Surgery</p>
  <div class="band"></div>
  <p class="abs center white site">www.silvermeadowsurgery.com</p>
</section>

<section class="sheet envelope" aria-label="Envelope">
  <div class="brand"><span class="brand-dot"></span>BLMRC</div>
  <p class="abs center tagline">Dental Implants and Oral Surgery</p>
  <div class="rule divider"></div>
  <p class="abs name doc-a">Martin K. Hale, DDS, Inc.</p>
  <p class="abs name doc-b">Yu Jin Park, DMD, MD, Inc.</p>
  <p class="abs addr" style="top:76px">3187 Silver Meadow Parkway, Cedar Ridge, CA 95118</p>
  <div class="rule green-rule" style="top:86px"></div>
  <p class="abs addr" style="top:89px">612 Lorin Way, Suite 101, Marlow, CA. 95241</p>
  <div class="rule green-rule" style="top:99px"></div>
  <p class="abs addr" style="top:102px">2375 Birch Avenue, Suite 105, Linden Falls, CA. 95377</p>
  <p class="abs center services">Dentoalveolar Surgery<span class="sep">•</span>Dental Implant Surgery<span class="sep">•</span>Orthognathic Surgery<span class="sep">•</span>Facial Trauma Surgery<span class="sep">•</span>Preprosthetic and Reconstructive Surgery<br>Temporomandibular Joint Disorders and Surgery<span class="sep">•</span>Obstructive Sleep Apnea Surgery</p>
  <div class="band"></div>
  <p class="abs center white site">www.silvermeadowsurgery.com</p>
</section>

</body>
</html>
```